Need a book cover design for a Lumora Book on Herbal Remedies

I need a book cover for my new ebook, here are the details:
Title: Meadow Cures
Sub-Heading: Buried Ancient Garden Tonics
Reclaiming the Wisdom of Roots for Everyday Wellness and Strength
Author: Nora Belcourt

```html
<!DOCTYPE html>
<html lang="en">
<head>
<meta charset="utf-8">
<title>Meadow Cures — Nora Belcourt</title>
<link rel="stylesheet" href="https://fonts.googleapis.com/css2?family=Montserrat:wght@500;600&family=Playfair+Display:wght@600;700&display=swap">
<style>
  :root {
    --page: #ffffff;
    --leaf-green: #8aab05;
    --ink: #2b2b2b;
    --title-white: #ffffff;
    --amber: #f7931e;
    --amber-band: #ff9a0a;
    --author-tint: #e8f5a6;
    --herb-dark: #6e7a2a;
    --herb-light: #b89a5a;
  }
  html, body {
    margin: 0;
    width: 1200px;
    height: 1200px;
    overflow: hidden;
    background: var(--page);
  }
  .cover {
    position: absolute;
    left: 200px;
    top: 0;
    width: 800px;
    height: 1200px;
    background: var(--page);
    box-shadow: 0 0 14px rgba(0,0,0,0.25);
    overflow: hidden;
  }
  .cover__top-band {
    position: absolute;
    left: 0; top: 0;
    width: 800px; height: 683px;
    background: var(--leaf-green);
  }
  .cover__artwork {
    position: absolute;
    left: 420px; top: 185px;
    width: 380px; height: 570px;
    border-radius: 40% 20% 30% 30%;
    background: radial-gradient(ellipse at 55% 55%, var(--herb-light) 0%, var(--herb-dark) 55%, rgba(110,122,42,0) 75%);
  }
  .cover__tagline {
    position: absolute;
    left: 108px; top: 160px;
    margin: 0;
    font-family: "Montserrat", sans-serif;
    font-weight: 600;
    font-size: 37px;
    line-height: 47px;
    color: var(--ink);
  }
  .cover__title {
    position: absolute;
    left: 100px; top: 500px;
    margin: 0;
    font-family: "Playfair Display", serif;
    font-weight: 700;
    line-height: 1;
  }
  .cover__title-first {
    display: block;
    font-size: 148px;
    color: var(--title-white);
    font-weight: 600;
  }
  .cover__title-second {
    display: block;
    margin-top: 24px;
    font-size: 150px;
    color: var(--amber);
  }
  .cover__subtitle {
    position: absolute;
    left: 106px; top: 830px;
    margin: 0;
    font-family: "Playfair Display", serif;
    font-weight: 600;
    font-size: 52px;
    line-height: 64px;
    color: var(--amber);
  }
  .cover__author {
    position: absolute;
    left: 96px; top: 1105px;
    width: 477px; height: 95px;
    background: var(--amber-band);
    box-sizing: border-box;
    padding-left: 38px;
    font-family: "Montserrat", sans-serif;
    font-weight: 500;
    font-size: 43px;
    line-height: 95px;
    color: var(--author-tint);
    margin: 0;
  }
</style>
</head>
<body>
  <main class="cover">
    <div class="cover__top-band"></div>
    <div class="cover__artwork" role="img" aria-label="Brass mortar and pestle filled with fresh herbs, with ginger root and peppercorns"></div>
    <p class="cover__tagline">Reclaiming<br>the Wisdom<br>of Roots for<br>Everyday Wellness<br>and Strength</p>
    <h1 class="cover__title">
      <span class="cover__title-first">Meadow</span>
      <span class="cover__title-second">Cures</span>
    </h1>
    <h2 class="cover__subtitle">Buried Ancient<br>Garden Tonics</h2>
    <p class="cover__author">Nora Belcourt</p>
  </main>
</body>
</html>
```